Business Card Logo for an Accountant (a Steady Ledger)

I would like a logo to put on my business card for an accountant. I am seasoned, skilled and give TLC to my clients. I have over 40 years of experience and love to teach people how to do accounting for their businesses. I am an accountant who can envision a fix to any problem.

Business Card will have this on it:

Loretta Quimbeck
dba Steady Ledger
Cell (555) 417-3082

```html
<!DOCTYPE html>
<html lang="en">
<head>
<meta charset="utf-8">
<title>Loretta Quimbeck – Business Card</title>
<link href="https://fonts.googleapis.com/css2?family=Lato:wght@400;700;900&display=swap" rel="stylesheet">
<style>
  :root {
    --backdrop: #3b3b3c;
    --crimson: #9b2238;
    --paper: #ffffff;
    --ink: #222222;
    --shadow: rgba(0,0,0,0.45);
  }
  * { margin: 0; padding: 0; box-sizing: border-box; }
  html, body { width: 1200px; height: 900px; overflow: hidden; }
  body {
    background: var(--backdrop);
    font-family: "Lato", sans-serif;
    position: relative;
  }
  .card {
    position: absolute;
    width: 580px;
    height: 330px;
    box-shadow: 0 14px 30px var(--shadow);
    overflow: hidden;
  }
  .card--front {
    left: 310px;
    top: 80px;
    background: var(--crimson);
    display: flex;
    align-items: center;
    justify-content: center;
  }
  .card--back {
    left: 310px;
    top: 480px;
    background: var(--paper);
  }
  .brand {
    display: flex;
    align-items: center;
    gap: 16px;
    font-weight: 900;
    line-height: 1.02;
  }
  .brand__square {
    width: 22px;
    height: 22px;
    flex: none;
  }
  .card--front .brand { color: var(--paper); font-size: 44px; }
  .card--front .brand__square { background: var(--paper); width: 30px; height: 30px; }
  .card--back .brand {
    position: absolute;
    left: 34px;
    top: 112px;
    color: var(--crimson);
    font-size: 27px;
  }
  .card--back .brand__square { background: var(--crimson); }
  .divider {
    position: absolute;
    left: 300px;
    top: 96px;
    width: 2px;
    height: 110px;
    background: var(--crimson);
  }
  .contact {
    position: absolute;
    left: 328px;
    top: 110px;
    color: var(--ink);
  }
  .contact__name {
    color: var(--crimson);
    font-weight: 700;
    font-size: 25px;
    line-height: 1.1;
  }
  .contact__dba {
    font-size: 19px;
    margin-top: 2px;
  }
  .contact__phone {
    display: flex;
    align-items: center;
    gap: 10px;
    font-size: 20px;
    margin-top: 8px;
  }
  .contact__icon { width: 12px; height: 18px; flex: none; }
  .card__band {
    position: absolute;
    left: 0;
    bottom: 0;
    width: 100%;
    height: 16px;
    background: var(--crimson);
  }
</style>
</head>
<body>
  <section class="card card--front">
    <div class="brand">
      <span class="brand__square"></span>
      <span class="brand__name">Loretta<br>Quimbeck</span>
    </div>
  </section>

  <section class="card card--back">
    <div class="brand">
      <span class="brand__square"></span>
      <span class="brand__name">Loretta<br>Quimbeck</span>
    </div>
    <div class="divider"></div>
    <div class="contact">
      <p class="contact__name">Loretta Quimbeck</p>
      <p class="contact__dba">dba Steady Ledger</p>
      <p class="contact__phone">
        <svg class="contact__icon" viewBox="0 0 12 18" aria-hidden="true">
          <rect x="1" y="1" width="10" height="16" rx="1.5" fill="none" stroke="#9b2238" stroke-width="1.5"/>
          <rect x="3" y="3.5" width="6" height="5" fill="#9b2238"/>
          <circle cx="6" cy="13.5" r="1.2" fill="#9b2238"/>
        </svg>
        <span>(555) 417-3082</span>
      </p>
    </div>
    <div class="card__band"></div>
  </section>
</body>
</html>
```